Home Page Design for Motor Manufacturer

Hello,
please design the homepage for a manufacturer of industry motors. I am looking for a professional, clean and minimalistic design. Since this a rather conservative industry it should get a professional look but since it is a redesign there should be some modern that gives is the modern touch of innovation.
A competitor's homepage I like is:
https://www.valtrosk.com/en/
What I like about this website:
* clean, minimal, well structured design
* mega menu
For this project please find attached the wireframes (most buttons are in German but by context and Google translate you will easily figure it out; only unclear - "Messe" means "trade exhibition"). The paddings and margins are NOT exact. Also any color of backgrounds etc. chosen is not meant to represent a real color but rather to illustrate the object and maybe show there should be some background emphasis (color or image).
Wireframes:
https: //www.filmavek. com / t / pxuTQmD7ZJHaLrwY
In both wireframes the only thing that is different is the Service section. I expect from the winner both designs for this service section: one with normal cart design and one with tabs as filters to search products (find image for product categories attached)
In the header use on the left the following text:
h1: "Your competent partner for industrial engines,
-transmission and drawing parts
with more than 5000 satisfied customers "
primary button: Our products
sec. button: Download catalog
and on the right side we feature one or more product images (like putting them in a nice display together).
I also think of a solid background color or subtle gradient for the hero section.
The winner should also design an open mega menu version.
Menu items in this order:
• Home page
• Gearboxes & Motors
• Engine components
• Drawing parts
• Machines & accessories
• About us
• Contact
Also create a language switch with globe symbol and DE for Germany and EN for English above the nav plus the telephone number with icon (user dummy number +49 (0) 987654321)
Output should be in Figma, Sketch or PSD.
Fonts + color to use:
header: Proza Libre, bold, # 0171A1
body: Open Sans, regular, black
Primary accent color: # 0171A1
Text black or dark gray
background: light gray, white or shade of blue
More image resources:
https://www.filmavek.com/t/QrnLVdHZPKEX1bmu
If there are any questions please do not hesitate to ask.
Target Market(s)
B2B - anyone with industrial machinery needing small motors (not car engines)
Industry/Entity Type
Manufacturing
Number of Pages Required
1 page
Requirements
Must have
- see above
Nice to have
- see above
Should not have
- see above

```html
<!DOCTYPE html>
<html lang="en">
<head>
<meta charset="utf-8">
<title>KORVANT – Industrial Motors &amp; Gearboxes</title>
<link href="https://fonts.googleapis.com/css2?family=Open+Sans:wght@400;600;700&family=Proza+Libre:wght@500;600;700&display=swap" rel="stylesheet">
<style>
:root{
  --accent:#0171A1;
  --accent-dark:#015b82;
  --ink:#111111;
  --text:#333333;
  --muted:#8a8a8a;
  --light:#f2f2f2;
  --line:#e3e3e3;
  --white:#ffffff;
  --orange:#f5a623;
  --sky:#a8d2dc;
  --bar:#2a2a2a;
}
*{box-sizing:border-box;margin:0;padding:0}
html,body{width:1200px;height:4498px;overflow:hidden}
body{font-family:"Open Sans",sans-serif;color:var(--text);background:var(--white);font-size:11px;line-height:1.6}
h1,h2,h3,h4{font-family:"Proza Libre",sans-serif;color:var(--ink);font-weight:700;line-height:1.2}
.section{position:relative;width:1200px;overflow:hidden}
.abs{position:absolute}
.btn{display:inline-flex;align-items:center;justify-content:center;font-size:11px;font-weight:600;text-decoration:none;height:30px;padding:0 20px}
.btn-primary{background:var(--accent);color:var(--white)}
.btn-outline{border:1.5px solid var(--accent);color:var(--ink);background:var(--white)}
.btn-dark{background:var(--ink);color:var(--white)}
.round-arrow{position:absolute;width:28px;height:28px;border-radius:50%;background:var(--accent);display:flex;align-items:center;justify-content:center}

/* top bar */
.topbar{height:59px}
.logo{left:161px;top:12px;font-family:"Proza Libre",sans-serif;font-weight:700;font-size:28px;color:var(--accent);letter-spacing:1px;display:flex;align-items:center;gap:8px}
.logo .dot{width:14px;height:14px;border-radius:50%;background:var(--accent)}
.search{left:316px;top:11px;width:388px;height:38px;display:flex;border:1px solid var(--line);border-radius:19px;overflow:hidden}
.search .label{background:var(--accent);color:var(--white);font-size:10px;width:88px;display:flex;align-items:center;justify-content:center;border-radius:19px}
.search .field{flex:1;display:flex;align-items:center;padding-left:16px;color:var(--muted);font-size:11px}
.search .go{width:38px;display:flex;align-items:center;justify-content:center;border-left:1px solid var(--line)}
.phone{left:762px;top:15px;display:flex;gap:8px;align-items:center}
.phone small{display:block;font-size:7px;color:var(--muted);line-height:1}
.phone strong{color:var(--accent);font-size:12px}
.lang{left:913px;top:20px;display:flex;gap:8px;align-items:center;font-size:11px;color:var(--muted)}

/* nav */
.nav{height:49px;background:var(--accent)}
.nav ul{position:absolute;left:161px;top:0;height:49px;display:flex;gap:0;list-style:none;align-items:center}
.nav li{color:var(--white);font-size:11px;font-weight:700;margin-right:26px}
.nav .user{position:absolute;left:1014px;top:14px}

/* hero */
.hero{height:524px}
.hero-photo{inset:0;background:linear-gradient(115deg,#2d261f 0%,#5a4a3a 35%,#7a6a58 55%,#3c3a38 80%,#1e1d1c 100%)}
.hero-card{left:320px;top:124px;width:562px;height:261px;display:flex;box-shadow:0 4px 20px rgba(0,0,0,.25)}
.hero-main{width:374px;background:var(--white);padding:38px 0 0 24px}
.hero-main h1{color:var(--accent);font-size:29px;line-height:1.22}
.hero-main p{color:var(--ink);font-size:13px;margin-top:18px;line-height:1.5}
.hero-main .actions{margin-top:20px;display:flex;gap:14px}
.hero-side{width:188px;background:#efefef;text-align:center;padding-top:32px}
.hero-side .thumb{width:90px;height:90px;margin:0 auto;border-radius:50%;background:radial-gradient(circle,#d8d8d8,#8e8e8e)}
.hero-side p{color:var(--muted);font-size:11px;padding:20px 14px 0;line-height:1.5}
.hero-side .btn{margin-top:12px;height:28px}

/* features */
.features{height:241px}
.feature-row{left:192px;top:-73px;width:800px;display:flex;gap:2px}
.feature{width:199px;height:259px;background:var(--white);box-shadow:0 2px 10px rgba(0,0,0,.1);text-align:center;padding-top:30px}
.feature h3{font-size:18px;margin-top:10px}
.feature .rule{width:34px;height:2px;background:var(--accent);margin:10px auto}
.feature p{color:var(--muted);font-size:11px;line-height:1.35;padding:0 16px}
.feature .round-arrow{position:relative;margin:20px auto 0}

/* categories */
.categories{height:266px;background:var(--light)}
.categories h2{position:absolute;top:74px;width:100%;text-align:center;font-size:26px;font-weight:600}
.cat-row{left:161px;top:137px;display:flex;gap:32px}
.cat{width:120px;height:87px;background:var(--white);text-align:center;padding-top:16px;font-size:10px;color:var(--ink);font-weight:600}
.cat span{display:block;margin-top:10px}

/* products */
.products{height:526px}
.products h2{left:161px;top:69px;font-size:26px}
.tabs{left:687px;top:75px;display:flex;gap:10px}
.tab{height:32px;background:#efefef;font-size:10px;display:flex;align-items:center;justify-content:center;color:var(--ink)}
.tab.active{background:var(--accent);color:var(--white)}
.prod-row{left:161px;top:148px;display:flex;gap:31px}
.prod{position:relative;width:196px;height:332px;background:var(--white);box-shadow:0 2px 10px rgba(0,0,0,.08);text-align:center}
.prod .badge{position:absolute;left:0;top:0;background:var(--orange);color:var(--white);font-size:9px;padding:2px 8px}
.prod .pic{width:130px;height:120px;margin:28px auto 0;border-radius:8px;background:linear-gradient(135deg,#cfd6da,#6d7478)}
.prod h4{font-family:"Open Sans",sans-serif;font-size:12px;font-weight:600;margin-top:32px}
.prod p{color:var(--muted);font-size:10.5px;line-height:1.4;padding:6px 14px 0}
.prod .details{position:absolute;left:0;right:0;top:258px;height:36px;background:var(--accent);color:var(--white);font-weight:700;font-size:12px;display:flex;align-items:center;justify-content:center}
.prod .quick{position:absolute;left:0;right:0;top:294px;height:38px;font-weight:700;font-size:12px;color:var(--ink);display:flex;align-items:center;justify-content:center}

/* measure up */
.measure{height:1104px;background:var(--light)}
.measure h2{position:absolute;top:76px;width:100%;text-align:center;font-size:26px;font-weight:600}
.m-card{left:162px;width:868px;height:271px;background:var(--white);box-shadow:0 1px 6px rgba(0,0,0,.05)}
.m-card .circle{position:absolute;left:44px;top:41px;width:189px;height:189px;border-radius:50%;border:1px solid var(--line);display:flex;align-items:center;justify-content:center}
.m-card .circle i{width:130px;height:110px;border-radius:10px;background:linear-gradient(135deg,#d5d9dc,#5b6165)}
.m-card h3{position:absolute;left:263px;top:50px;font-size:18px;font-weight:600}
.m-card p{position:absolute;left:263px;top:84px;width:552px;font-size:10.5px;line-height:1.85;color:#555}
.m-card .actions{position:absolute;left:600px;top:190px;display:flex;gap:14px}
.m-card .btn{width:100px;height:32px;padding:0}

/* about */
.about{height:510px}
.about h2{left:161px;top:92px;font-size:27px}
.about .bar{left:162px;top:143px;width:60px;height:250px;background:var(--accent)}
.about .copy{left:248px;top:141px;width:330px}
.about .lead{font-weight:700;color:var(--ink);font-size:12px;line-height:1.75}
.about .copy p{font-size:10.5px;color:#555;margin-top:14px;line-height:1.75}
.about .btn{margin-top:16px;width:114px;padding:0;height:36px}
.about .big{left:673px;top:84px;width:366px;height:366px;border-radius:50%;border:4px solid var(--accent);background:linear-gradient(140deg,#b89878,#e4d6c4 45%,#8e7b66)}
.about .small{left:596px;top:231px;width:220px;height:220px;border-radius:50%;border:4px solid var(--accent);background:radial-gradient(circle at 55% 50%,#3a3f44,#c8cdd1 70%,#eef0f1)}

/* downloads */
.downloads{height:500px;background:#f4f4f4}
.downloads .photo{left:0;top:0;width:601px;height:500px;background:linear-gradient(135deg,#1a1c1e,#5b6066 40%,#2b2e31 70%,#101112)}
.downloads h2{left:662px;top:88px;font-size:28px;font-weight:600}
.downloads .text{left:662px;top:140px;width:380px}
.downloads .text p{font-size:10.5px;color:#555;line-height:1.7;margin-bottom:18px}
.downloads .btn{position:absolute;left:667px;top:394px;width:136px;height:36px;padding:0;gap:4px}

/* contact */
.contact{height:271px;background:linear-gradient(180deg,#b6dce4,#9fcbd6)}
.contact h2{position:absolute;top:58px;width:100%;text-align:center;font-size:27px;font-weight:600}
.contact .in{top:120px;width:240px;height:35px;background:var(--white);font-size:11px;color:var(--muted);display:flex;align-items:center;padding-left:18px}
.contact .btn{position:absolute;left:536px;top:188px;width:128px;height:35px;padding:0}

/* info */
.info{height:143px}
.info .item{top:36px;display:flex;gap:12px}
.info h4{font-family:"Open Sans",sans-serif;font-size:12px;font-weight:600;color:var(--ink)}
.info p{font-size:10px;color:var(--muted);line-height:1.45}
.info .btn{position:absolute;left:917px;top:50px;width:123px;height:34px;padding:0}
.info .rule{left:161px;top:142px;width:879px;height:1px;background:var(--line)}

/* footer */
.footer{height:253px}
.footer h4{font-family:"Open Sans",sans-serif;font-size:12px;font-weight:600;color:var(--ink)}
.footer ul{list-style:none;margin-top:14px}
.footer li{font-size:10px;color:var(--muted);line-height:24px}
.news{left:692px;top:39px;width:348px}
.news p{font-size:10px;color:var(--muted);line-height:24px}
.news .form{display:flex;margin-top:12px;height:38px}
.news .form span{flex:1;border:1px solid var(--line);font-size:10px;color:var(--muted);display:flex;align-items:center;padding-left:16px}
.news .form b{width:100px;background:var(--accent);color:var(--white);font-size:11px;font-weight:600;display:flex;align-items:center;justify-content:center}
.social{display:flex;gap:6px;margin-top:10px}
.social i{width:28px;height:28px;border-radius:50%;background:var(--accent)}
.bottom{height:52px;background:var(--bar);color:#ddd;font-size:10px}
.bottom .copy{left:161px;top:18px}
.bottom .links{right:160px;top:18px;display:flex;gap:16px}
</style>
</head>
<body>

<header class="section topbar">
  <div class="abs logo"><span class="dot"></span>KORVANT</div>
  <div class="abs search">
    <span class="label">Search Item</span>
    <span class="field">Search</span>
    <span class="go"><svg width="11" height="11" viewBox="0 0 12 12"><circle cx="5" cy="5" r="3.8" fill="none" stroke="#666" stroke-width="1.4"/><line x1="8" y1="8" x2="11" y2="11" stroke="#666" stroke-width="1.4"/></svg></span>
  </div>
  <div class="abs phone">
    <svg width="14" height="14" viewBox="0 0 24 24"><path d="M6.6 10.8a15 15 0 006.6 6.6l2.2-2.2a1 1 0 011-.25 11 11 0 003.6.6 1 1 0 011 1V20a1 1 0 01-1 1A17 17 0 013 4a1 1 0 011-1h3.5a1 1 0 011 1c0 1.25.2 2.45.6 3.6a1 1 0 01-.25 1z" fill="#0171A1"/></svg>
    <div><small>Call for Any Question</small><strong>+49 (0) 987654321</strong></div>
  </div>
  <div class="abs lang">
    <svg width="13" height="13" viewBox="0 0 24 24"><circle cx="12" cy="12" r="10" fill="#0171A1"/><path d="M2 12h20M12 2a15 15 0 010 20M12 2a15 15 0 000 20" stroke="#fff" stroke-width="1.5" fill="none"/></svg>
    <span>Select Language</span>
    <svg width="8" height="6" viewBox="0 0 8 6"><path d="M1 1l3 3 3-3" stroke="#666" fill="none" stroke-width="1.3"/></svg>
  </div>
</header>

<nav class="section nav">
  <ul>
    <li>Home</li>
    <li>Gearboxes &amp; Motors ▾</li>
    <li>Engine Components ▾</li>
    <li>Drawing Parts ▾</li>
    <li>Machines &amp; Accessories ▾</li>
    <li>About Us</li>
    <li>Contact</li>
  </ul>
  <svg class="user" width="20" height="20" viewBox="0 0 24 24"><circle cx="12" cy="8" r="4.5" fill="none" stroke="#fff" stroke-width="1.6"/><path d="M3.5 22c1-5 4.5-7 8.5-7s7.5 2 8.5 7" fill="none" stroke="#fff" stroke-width="1.6"/></svg>
</nav>

<section class="section hero">
  <div class="abs hero-photo" role="img" aria-label="Industrial factory hall with steel structures"></div>
  <div class="round-arrow" style="left:14px;top:356px;background:none">
    <svg width="12" height="14" viewBox="0 0 12 14"><path d="M8 2L3 7l5 5" stroke="#fff" stroke-width="2.4" fill="none"/></svg>
  </div>
  <div class="round-arrow" style="left:1130px;top:242px;width:42px;height:42px;background:#1e1e1e">
    <svg width="12" height="14" viewBox="0 0 12 14"><path d="M4 2l5 5-5 5" stroke="#fff" stroke-width="2.4" fill="none"/></svg>
  </div>
  <div class="abs hero-card">
    <div class="hero-main">
      <h1>Your competent partner<br>for industrial engines,</h1>
      <p>Transmission and drawing parts with more than<br>5000 satisfied customers</p>
      <div class="actions">
        <a class="btn btn-primary" style="width:114px;padding:0">Our Products</a>
        <a class="btn btn-outline" style="width:136px;padding:0">Download Catalog</a>
      </div>
    </div>
    <div class="hero-side">
      <div class="thumb" role="img" aria-label="Precision gearbox component"></div>
      <p>Lorem ipsum dolor sit amet, consectetur adipiscing elit.</p>
      <a class="btn btn-primary" style="width:90px;padding:0">View More</a>
    </div>
  </div>
</section>

<section class="section features" style="overflow:visible">
  <div class="abs feature-row">
    <div class="feature">
      <svg width="40" height="40" viewBox="0 0 40 40"><path d="M4 36V16l8 6v-6l8 6v-6l8 6V6h8v30z" fill="none" stroke="#0171A1" stroke-width="2"/><path d="M10 28h4M18 28h4M26 28h4" stroke="#0171A1" stroke-width="2"/></svg>
      <h3>Feature 01</h3><div class="rule"></div>
      <p>Lorem ipsum dolor sit amet, consectetur adipiscing elit. Donec faucibus consequat dui sit amet consequat.</p>
      <div class="round-arrow"><svg width="8" height="10" viewBox="0 0 8 10"><path d="M2 1l4 4-4 4" stroke="#fff" stroke-width="1.8" fill="none"/></svg></div>
    </div>
    <div class="feature">
      <svg width="40" height="40" viewBox="0 0 40 40"><path d="M4 36V16l8 6v-6l8 6v-6l8 6V6h8v30z" fill="none" stroke="#0171A1" stroke-width="2"/><path d="M10 28h4M18 28h4M26 28h4" stroke="#0171A1" stroke-width="2"/></svg>
      <h3>Feature 02</h3><div class="rule"></div>
      <p>Lorem ipsum dolor sit amet, consectetur adipiscing elit. Donec faucibus consequat dui sit amet consequat.</p>
      <div class="round-arrow"><svg width="8" height="10" viewBox="0 0 8 10"><path d="M2 1l4 4-4 4" stroke="#fff" stroke-width="1.8" fill="none"/></svg></div>
    </div>
    <div class="feature">
      <svg width="40" height="40" viewBox="0 0 40 40"><path d="M4 36V16l8 6v-6l8 6v-6l8 6V6h8v30z" fill="none" stroke="#0171A1" stroke-width="2"/><path d="M10 28h4M18 28h4M26 28h4" stroke="#0171A1" stroke-width="2"/></svg>
      <h3>Feature 03</h3><div class="rule"></div>
      <p>Lorem ipsum dolor sit amet, consectetur adipiscing elit. Donec faucibus consequat dui sit amet consequat.</p>
      <div class="round-arrow"><svg width="8" height="10" viewBox="0 0 8 10"><path d="M2 1l4 4-4 4" stroke="#fff" stroke-width="1.8" fill="none"/></svg></div>
    </div>
    <div class="feature">
      <svg width="40" height="40" viewBox="0 0 40 40"><path d="M4 36V16l8 6v-6l8 6v-6l8 6V6h8v30z" fill="none" stroke="#0171A1" stroke-width="2"/><path d="M10 28h4M18 28h4M26 28h4" stroke="#0171A1" stroke-width="2"/></svg>
      <h3>Feature 04</h3><div class="rule"></div>
      <p>Lorem ipsum dolor sit amet, consectetur adipiscing elit. Donec faucibus consequat dui sit amet consequat.</p>
      <div class="round-arrow"><svg width="8" height="10" viewBox="0 0 8 10"><path d="M2 1l4 4-4 4" stroke="#fff" stroke-width="1.8" fill="none"/></svg></div>
    </div>
  </div>
</section>

<section class="section categories">
  <h2>Product Categories</h2>
  <div class="round-arrow" style="left:113px;top:166px"><svg width="8" height="10" viewBox="0 0 8 10"><path d="M6 1L2 5l4 4" stroke="#fff" stroke-width="1.8" fill="none"/></svg></div>
  <div class="abs cat-row">
    <div class="cat"><svg width="30" height="28" viewBox="0 0 40 36"><path d="M4 34V14l8 6v-6l8 6v-6l8 6V4h8v30z" fill="none" stroke="#0171A1" stroke-width="2.2"/></svg><span>Category 01</span></div>
    <div class="cat"><svg width="30" height="28" viewBox="0 0 40 36"><path d="M4 34V14l8 6v-6l8 6v-6l8 6V4h8v30z" fill="none" stroke="#0171A1" stroke-width="2.2"/></svg><span>Category 02</span></div>
    <div class="cat"><svg width="30" height="28" viewBox="0 0 40 36"><path d="M4 34V14l8 6v-6l8 6v-6l8 6V4h8v30z" fill="none" stroke="#0171A1" stroke-width="2.2"/></svg><span>Category 03</span></div>
    <div class="cat"><svg width="30" height="28" viewBox="0 0 40 36"><path d="M4 34V14l8 6v-6l8 6v-6l8 6V4h8v30z" fill="none" stroke="#0171A1" stroke-width="2.2"/></svg><span>Category 04</span></div>
    <div class="cat"><svg width="30" height="28" viewBox="0 0 40 36"><path d="M4 34V14l8 6v-6l8 6v-6l8 6V4h8v30z" fill="none" stroke="#0171A1" stroke-width="2.2"/></svg><span>Category 05</span></div>
    <div class="cat"><svg width="30" height="28" viewBox="0 0 40 36"><path d="M4 34V14l8 6v-6l8 6v-6l8 6V4h8v30z" fill="none" stroke="#0171A1" stroke-width="2.2"/></svg><span>Category 06</span></div>
  </div>
  <div class="round-arrow" style="left:1058px;top:166px"><svg width="8" height="10" viewBox="0 0 8 10"><path d="M2 1l4 4-4 4" stroke="#fff" stroke-width="1.8" fill="none"/></svg></div>
</section>

<section class="section products">
  <h2 class="abs">Products</h2>
  <div class="abs tabs">
    <span class="tab" style="width:60px">All</span>
    <span class="tab active" style="width:101px">Subcat 01</span>
    <span class="tab" style="width:52px">Subcat</span>
    <span class="tab" style="width:101px">Subcat 03</span>
  </div>
  <div class="round-arrow" style="left:115px;top:300px"><svg width="8" height="10" viewBox="0 0 8 10"><path d="M6 1L2 5l4 4" stroke="#fff" stroke-width="1.8" fill="none"/></svg></div>
  <div class="abs prod-row">
    <div class="prod"><span class="badge">★ Featured</span><div class="pic" role="img" aria-label="Servo motor with gearbox"></div><h4>Product 01</h4><p>Lorem ipsum dolor sit amet, consectetur adipiscing elit. Proin eu felis felis.</p><div class="details">VIEW DETAILS</div><div class="quick">QUICK VIEW</div></div>
    <div class="prod"><div class="pic" role="img" aria-label="Right-angle planetary gearbox"></div><h4>Product 02</h4><p>Lorem ipsum dolor sit amet, consectetur adipiscing elit. Proin eu felis felis.</p><div class="details">VIEW DETAILS</div><div class="quick">QUICK VIEW</div></div>
    <div class="prod"><span class="badge">★ Featured</span><div class="pic" role="img" aria-label="Servo motor with gearbox"></div><h4>Product 03</h4><p>Lorem ipsum dolor sit amet, consectetur adipiscing elit. Proin eu felis felis.</p><div class="details">VIEW DETAILS</div><div class="quick">QUICK VIEW</div></div>
    <div class="prod"><div class="pic" role="img" aria-label="Right-angle planetary gearbox"></div><h4>Product 04</h4><p>Lorem ipsum dolor sit amet, consectetur adipiscing elit. Proin eu felis felis.</p><div class="details">VIEW DETAILS</div><div class="quick">QUICK VIEW</div></div>
  </div>
  <div class="round-arrow" style="left:1060px;top:300px"><svg width="8" height="10" viewBox="0 0 8 10"><path d="M2 1l4 4-4 4" stroke="#fff" stroke-width="1.8" fill="none"/></svg></div>
</section>

<section class="section measure">
  <h2>Measure Up</h2>
  <article class="abs m-card" style="top:148px">
    <div class="circle"><i role="img" aria-label="Right-angle gearbox"></i></div>
    <h3>Title Here</h3>
    <p>Lorem ipsum dolor sit amet, consectetur adipiscing elit. Proin eu felis felis. Donec at pellentesque enim. Quisque vehicula nunc felis, ut porttitor ipsum convallis quis. Praesent vel facilisis ex. Mauris cursus sit amet augue ut porttitor. Integer pellentesque risus vitae pellentesque fringilla. In ut imperdiet enim. Integer dolor ligula, malesuada a dolor non, congue eleifend tortor.</p>
    <div class="actions"><a class="btn btn-primary">Free Ticket</a><a class="btn btn-dark">View Details</a></div>
  </article>
  <article class="abs m-card" style="top:438px">
    <div class="circle"><i role="img" aria-label="Right-angle gearbox"></i></div>
    <h3>Title Here</h3>
    <p>Lorem ipsum dolor sit amet, consectetur adipiscing elit. Proin eu felis felis. Donec at pellentesque enim. Quisque vehicula nunc felis, ut porttitor ipsum convallis quis. Praesent vel facilisis ex. Mauris cursus sit amet augue ut porttitor. Integer pellentesque risus vitae pellentesque fringilla. In ut imperdiet enim. Integer dolor ligula, malesuada a dolor non, congue eleifend tortor.</p>
    <div class="actions"><a class="btn btn-primary">Free Ticket</a><a class="btn btn-dark">View Details</a></div>
  </article>
  <article class="abs m-card" style="top:732px">
    <div class="circle"><i role="img" aria-label="Right-angle gearbox"></i></div>
    <h3>Title Here</h3>
    <p>Lorem ipsum dolor sit amet, consectetur adipiscing elit. Proin eu felis felis. Donec at pellentesque enim. Quisque vehicula nunc felis, ut porttitor ipsum convallis quis. Praesent vel facilisis ex. Mauris cursus sit amet augue ut porttitor. Integer pellentesque risus vitae pellentesque fringilla. In ut imperdiet enim. Integer dolor ligula, malesuada a dolor non, congue eleifend tortor.</p>
    <div class="actions"><a class="btn btn-primary">Free Ticket</a><a class="btn btn-dark">View Details</a></div>
  </article>
</section>

<section class="section about">
  <h2 class="abs">About Us</h2>
  <div class="abs bar"></div>
  <div class="abs copy">
    <div class="lead">Lorem ipsum dolor sit amet, consectetur adipiscing elit. Proin eu felis felis. Donec at pellentesque enim.</div>
    <p>Lorem Ipsum is simply dummy text of the printing and typesetting industry. Lorem Ipsum has been the industry's standard dummy text ever since the 1500s Lorem ipsum is simply dummy text of the printing and typesetting industry.</p>
    <p>Lorem ipsum dolor sit amet, consectetur adipiscing elit. Proin eu felis felis.</p>
    <a class="btn btn-dark">Read More</a>
  </div>
  <div class="abs big" role="img" aria-label="Workspace desk with coffee mug and notebook"></div>
  <div class="abs small" role="img" aria-label="Compact electric gear motor"></div>
</section>

<section class="section downloads">
  <div class="abs photo" role="img" aria-label="Close-up of engine belts and pulleys"></div>
  <h2 class="abs">Downloads</h2>
  <div class="abs text">
    <p>Lorem ipsum dolor sit amet, consectetur adipiscing elit. Proin eu felis felis. Donec at pellentesque enim. Quisque vehicula nunc felis, ut porttitor ipsum convallis quis. Praesent vel facilisis ex. Mauris cursus sit amet augue ut porttitor. Integer pellentesque risus vitae pellentesque fringilla. In imperdiet enim. Integer dolor ligula, malesuada a dolor non, congue eleifend tortor. Sed feugiat odio nec diam vulputate malesuada.</p>
    <p>Lorem ipsum dolor sit amet, consectetur adipiscing elit. Proin eu felis felis. Donec at pellentesque enim. Quisque vehicula nunc felis, ut porttitor ipsum convallis quis. Praesent vel facilisis ex. Mauris cursus sit amet augue ut porttitor. Integer pellentesque risus vitae pellentesque fringilla. In imperdiet enim. Integer dolor ligula, malesuada a dolor non, congue eleifend tortor. Sed feugiat odio nec diam vulputate malesuada.</p>
  </div>
  <a class="btn btn-outline">DOWNLOAD <svg width="10" height="10" viewBox="0 0 10 10"><path d="M5 1v5M2.5 4L5 6.5 7.5 4M1 9h8" stroke="#111" stroke-width="1.6" fill="none"/></svg></a>
</section>

<section class="section contact">
  <h2>Contact Us</h2>
  <div class="abs in" style="left:356px">Phone</div>
  <div class="abs in" style="left:604px">Email Address</div>
  <a class="btn btn-primary">SUBMIT</a>
</section>

<section class="section info">
  <div class="abs item" style="left:161px">
    <svg width="56" height="56" viewBox="0 0 56 56"><path d="M28 6a13 13 0 0113 13c0 10-13 24-13 24S15 29 15 19A13 13 0 0128 6z" fill="none" stroke="#0171A1" stroke-width="2"/><circle cx="28" cy="19" r="5" fill="none" stroke="#0171A1" stroke-width="2"/><path d="M18 38l-12 12h44L38 38" fill="none" stroke="#0171A1" stroke-width="2"/></svg>
    <div><h4>Address</h4><p>Lorem ipsum dolor sit<br>amet,</p></div>
  </div>
  <div class="abs item" style="left:402px">
    <svg width="56" height="56" viewBox="0 0 56 56"><path d="M6 20c0-8 44-8 44 0v4h-10v-6H16v6H6z" fill="none" stroke="#0171A1" stroke-width="2"/><rect x="12" y="26" width="32" height="22" rx="3" fill="none" stroke="#0171A1" stroke-width="2"/><text x="28" y="42" text-anchor="middle" font-size="12" font-weight="700" fill="#0171A1" font-family="Open Sans, sans-serif">24</text></svg>
    <div><h4>Contact Info</h4><p>+49 (0) 987654321<br>+49 (0) 987654321</p></div>
  </div>
  <div class="abs item" style="left:633px">
    <svg width="56" height="56" viewBox="0 0 56 56"><rect x="6" y="18" width="44" height="30" fill="none" stroke="#0171A1" stroke-width="2"/><path d="M6 18l22 16 22-16M6 48l16-14M50 48L34 34" fill="none" stroke="#0171A1" stroke-width="2"/><rect x="16" y="6" width="24" height="18" fill="#fff" stroke="#0171A1" stroke-width="2"/><path d="M20 12h16M20 17h12" stroke="#0171A1" stroke-width="2"/></svg>
    <div><h4>Email Address</h4><p>info@example.com<br>info@example.com</p></div>
  </div>
  <a class="btn btn-primary">Get in Touch</a>
  <div class="abs rule"></div>
</section>

<footer class="section footer">
  <div class="abs" style="left:161px;top:39px"><h4>OUR SOLUTIONS</h4>
    <ul><li>Lorem ipsum is dolor</li><li>Lorem ipsum is dolor</li><li>Lorem ipsum is dolor</li><li>Lorem ipsum is dolor</li><li>Lorem ipsum is dolor</li></ul></div>
  <div class="abs" style="left:389px;top:39px"><h4>COMPANY</h4>
    <ul><li>Home</li><li>Company News</li><li>Case Study</li><li>Awards</li><li>Contact Us</li></ul></div>
  <div class="abs" style="left:537px;top:59px">
    <ul><li>About Us</li><li>Products</li><li>Faq's</li><li>Services</li><li>Our Team</li></ul></div>
  <div class="abs news"><h4>SUBSCRIBE OUR NEWSLETTER</h4>
    <p style="margin-top:12px">Weekly Breaking News Analysis And Cutting Edge<br>Advices On Job Searching.</p>
    <div class="form"><span>Email Address</span><b>SUBSCRIBE</b></div>
    <div class="social"><i></i><i></i><i></i><i></i></div>
  </div>
</footer>

<div class="section bottom">
  <span class="abs copy">Copyright © 2020. All Rights Reserved.</span>
  <span class="abs links"><span>Home</span><span>About</span><span>FAQs</span><span>Contact</span></span>
</div>

</body>
</html>
```